Flyer for a new laundromat (coin laundry)

Name of our new laundromat is Washhouse Tovi. Website will be washhousetovi.com.au (not created yet). Phone number is 07 4829 35172. Address is 27 Harlow Street, Woodridge QLD 4114. Our target audience is 30-50 year olds from a low socio-economic background. The neighbourhood is multicultural and has people from many different countries living together in unity.The flyer should be simple, easy to understand, with pictures as not everyone will have strong background in English. It will be good for the flyer to somehow indicate multiculturalism, unity and community spirit although I am not sure how this would be represented. The purpose of the flyer is to announce the opening of the laundromat.

We want to see a sunflower in place of the letter "O" in the word "Laundromat" as this is our logo.

We want the following elements/text included in the flyer:

a location map & shop address (27 Harlow Street, Woodridge, QLD 4114
"24 hours access through Grocerly"
"plenty of parking"
"Fast Jumbo washers - wash all your blankets or upto 4 laundry loads at once"
"Express gas tumble dryers from Sweden to dry your clothes in no time!"
"Free detergent - free detergent is added automatically in all our front load washers for your convenience or use our modern top loaders if you prefer using your own detergents "
"Amazing prices: Jumbo Washers $8, $4 double front load washers, $4 extra capacity top load washers, $1 dryers. free detergent"

Target Market(s)

30-60

Industry/Entity Type

Coin

Requirements
Must have
• Sunflower in the word "Laundromat"
• Good use of pictures, low on text, big on pictures / graphics
• Must promote "free detergent" and our low prices
• Show a google map for location
Nice to have
• Would be good to see an element of diversity and multicultaralism reflected in the flyer
• Fun element in flyer
Should not have
• Too much text
• Must not look too sophisticated as we are dealing with low socio econimic clientele here

```html
<!DOCTYPE html>
<html lang="en">
<head>
<meta charset="utf-8">
<title>Washhouse Tovi – Grand Opening</title>
<link href="https://fonts.googleapis.com/css2?family=Lato:ital,wght@0,400;0,700;0,900;1,400;1,700&family=Oswald:wght@600;700&display=swap" rel="stylesheet">
<style>
:root{
  --orange:#f26a1e;
  --orange-light:#f7941d;
  --orange-deep:#e4561a;
  --charcoal:#3d3d3f;
  --ink:#2b2b2b;
  --paper:#f4f4f4;
  --white:#ffffff;
}
*{margin:0;padding:0;box-sizing:border-box}
html,body{width:825px;height:1200px;overflow:hidden;background:#e9e9e9}
.flyer{position:relative;width:825px;height:1200px;overflow:hidden;
  background:linear-gradient(180deg,#f7f7f7 0%,#eeeeee 55%,#f3f3f3 100%);
  font-family:"Lato",sans-serif;color:var(--ink)}
.hero-photo{position:absolute;left:0;top:0;width:520px;height:420px;
  background:linear-gradient(120deg,#ffffff 0%,#e8e6e4 45%,#d9d7d5 75%,#eeeeee 100%)}
.hero-swoosh{position:absolute;left:0;top:300px;width:825px;height:170px}
.headline{position:absolute;right:36px;top:48px;text-align:right;line-height:1}
.headline .grand{display:block;font-weight:900;font-size:92px;color:var(--charcoal);letter-spacing:-1px}
.headline .opening{display:block;font-weight:900;font-size:78px;color:var(--orange);margin-top:8px}
.call{position:absolute;left:440px;top:270px;width:400px;height:56px;border-radius:28px 0 0 28px;
  background:linear-gradient(90deg,var(--orange-deep),var(--orange-light));
  border:4px solid var(--charcoal);border-right:none;
  color:var(--white);font-weight:900;font-size:31px;line-height:48px;padding-left:26px}
.prices{position:absolute;left:43px;top:448px;width:750px;display:flex;justify-content:space-between}
.price-tag{position:relative;width:162px;height:160px;border-radius:14px 14px 34px 34px;overflow:hidden;
  background:linear-gradient(180deg,var(--orange-light) 0%,var(--orange) 55%,var(--orange-deep) 100%);
  color:var(--white);text-align:center;font-family:"Oswald",sans-serif;text-transform:uppercase;
  box-shadow:0 4px 6px rgba(0,0,0,.18)}
.price-tag::before{content:"";position:absolute;left:0;top:0;width:0;height:0;
  border-top:70px solid rgba(255,255,255,.16);border-right:162px solid transparent}
.price-tag .amount{display:block;font-size:72px;font-weight:700;line-height:1;margin-top:10px}
.price-tag .label{display:block;font-size:20px;font-weight:600;line-height:1.05;margin-top:2px}
.price-tag .label.small{font-size:15px}
.price-tag .label.big{font-size:28px}
.dark-panel{position:absolute;left:0;top:0;width:825px;height:1200px}
.features{position:absolute;left:27px;top:668px;width:460px;list-style:none;font-style:italic;font-size:18.5px;line-height:1.38;color:var(--ink)}
.features li{position:relative;padding-left:30px;margin-bottom:20px}
.features li.plain{margin-top:-8px}
.features li.dot::before{content:"";position:absolute;left:0;top:8px;width:13px;height:13px;border-radius:50%;background:var(--orange)}
.features strong{color:var(--orange);font-weight:700}
.basket-photo{position:absolute;left:520px;top:705px;width:300px;height:215px;border-radius:8px;
  background:radial-gradient(ellipse at 50% 55%,#d8232a 0%,#b51e24 45%,rgba(70,70,72,0) 75%)}
.map{position:absolute;left:540px;top:932px;width:262px;height:134px;border:6px solid var(--orange);border-radius:24px;
  background:linear-gradient(135deg,#eceae4 0%,#e3e1da 50%,#d9e6cf 100%)}
.address{position:absolute;left:500px;top:1082px;width:320px;text-align:center;color:var(--white);font-weight:700;font-size:15.5px}
.brand{position:absolute;left:36px;top:1000px;display:flex;align-items:center;gap:12px}
.brand .mark{width:28px;height:28px;border-radius:50%;background:var(--orange-light)}
.brand .name{font-weight:700;font-size:46px;color:var(--orange);letter-spacing:-.5px}
.footer{position:absolute;left:0;bottom:0;width:825px;height:70px;
  background:linear-gradient(90deg,var(--orange-deep),var(--orange-light));
  color:var(--white);font-size:17px;font-weight:700;letter-spacing:3px;text-align:center;line-height:70px}
</style>
</head>
<body>
<main class="flyer">
  <div class="hero-photo" role="img" aria-label="Photo of a woman loading a pink towel into a front-load washing machine"></div>

  <svg class="hero-swoosh" viewBox="0 0 825 170" preserveAspectRatio="none" aria-hidden="true">
    <path d="M0 80 C120 150 260 150 420 125 C560 105 700 110 825 150 L825 170 L0 170 Z" fill="#f2f2f2"/>
    <path d="M0 70 C120 140 260 140 420 112 C560 92 700 100 825 135 L825 150 C700 118 560 112 420 130 C260 156 120 158 0 95 Z" fill="var(--orange)"/>
    <path d="M0 60 C120 122 260 124 420 100 C560 80 700 88 825 118 L825 126 C700 96 560 90 420 110 C260 134 120 134 0 72 Z" fill="var(--charcoal)"/>
  </svg>

  <h1 class="headline"><span class="grand">Grand</span><span class="opening">Opening</span></h1>
  <div class="call">Call: 07 4829 35172</div>

  <section class="prices">
    <div class="price-tag"><span class="amount">$8</span><span class="label">Jumbo<br>Washers</span></div>
    <div class="price-tag"><span class="amount">$4</span><span class="label small">Double Front<br><span style="font-size:20px">Load Washers</span></span></div>
    <div class="price-tag"><span class="amount">$4</span><span class="label small">Extra Capacity<br><span style="font-size:20px">Top Load<br>Washers</span></span></div>
    <div class="price-tag"><span class="amount">$1</span><span class="label big">Free</span><span class="label">Detergent</span></div>
  </section>

  <svg class="dark-panel" viewBox="0 0 825 1200" aria-hidden="true">
    <path d="M825 600 C650 690 500 880 430 1130 L825 1130 Z" fill="var(--orange)"/>
    <path d="M825 625 C670 710 530 890 470 1130 L825 1130 Z" fill="var(--charcoal)"/>
  </svg>

  <ul class="features">
    <li class="dot"><strong>Free detergent</strong> - free detergent is added automatically in all our front load washers for your convenience or use our modern top loaders if you prefer using your own detergents</li>
    <li class="dot">24 hours access through Grocerly</li>
    <li class="plain">Plenty of parking</li>
    <li class="dot"><strong>Fast Jumbo washers</strong> - wash all your blankets or upto 4 laundry loads at once</li>
    <li class="dot">Express gas tumble dryers from Sweden to dry your clothes in no time!</li>
  </ul>

  <div class="basket-photo" role="img" aria-label="Photo of a red laundry basket overflowing with clothes"></div>
  <div class="map" role="img" aria-label="Street map showing the shop location on Harlow Street, Woodridge"></div>
  <p class="address">27 Harlow Street, Woodridge, QLD 4114</p>

  <div class="brand"><span class="mark"></span><span class="name">Washhouse Tovi</span></div>

  <footer class="footer">Please visit us to know more about us at: washhousetovi.com.au</footer>
</main>
</body>
</html>
```